Plastic Surgeon Stationary Design

I Already have the logo. I Want and a clean, minimalist and elegant project. Please, I prefer Black, White and Gold color but you're free to try another ones. Business card,
Letterhead (A4 and Office), Recipes (Letter Pad) (A5), Envelop, Invoice, Computer Bill, Bill Book, Single A4 page size,
You Have to create at least the same materials I already own. I would like to a file to use in word to print letterheads and letter pad.
What I want that you make more changes are the envelopes that are to colorful and not elegant.
I'll not accept any design without my addresses as you can guide yourself with the models I provide.
Here are the addresses too:
"www.rubemtavorasilva.example" (website)
(My clinics' address)
"VILA AURORA
Rua Lucas Bentim, 3180, Lucas Bentim Office, Cj 204
Vila Aurora - VA
(11) 90123-4567"
"PORTO CELESTE
Rua Clemente Vilaça, 418, 7° andar
Edificio Torre Quaresma
Porto Celeste - PC
(047) 9012-3456"
Attention: Letterheads, Recipes, have to contain "CRM/SC 52.807 and CRM/SP 308.614" close to my name (Dr. Rubem Távora - Cirurgião Plástico), it is usually placed at the bottom.
Designers, attention!
During the process of creating bear in mind that the details of the logo, as the faces on the sides, are designed to be subtle. Highlight other such details affect the delicacy and elegance of the logo and visual identity.
When you are creating stationery, do not abuse the use of the logo, it should be used once or at most two times in each item.
Remember! Each stationery set must submit 3 models, one with the address "Balneario Camboriu", another with the address of "Vila Aurora" and the third containing both addresses.
The model letter envelope, folder type bag for letterhead and folder with inner pocket that provided a model did not please me because they are very flashy. Give preference to the use of white or black background.
PLEASE! Seek inspiration in the models contained in this link:
https://www.filecrate.example/sh/kq27zp41wcx905m/PlRtVuY_QX
In this link you can find my PAST Stationary Itens, so it can help you on your work
https://docuvault.example/7ZK3NB8QeT2LwYhR
Reason: Nobody presented anything useful.
Reason: still waiting some designers send their projects
Reason: Still Waiting Some Designs....
Target Market(s)
Mostly females with good economical condition. (Class A and AB)
Industry/Entity Type
Business
Requirements
Must have
- You have to provide 3 models of each paper, one with the address of Vila Aurora, another with the Balneario Camboriú address, and the third one with both addresses.

```html
<!DOCTYPE html>
<html lang="pt-BR">
<head>
<meta charset="utf-8">
<title>Rubem Távora — Papelaria</title>
<link rel="stylesheet" href="https://fonts.googleapis.com/css2?family=Playfair+Display:wght@600&family=Tinos&family=Montserrat:wght@400;500&family=Great+Vibes&display=swap">
<style>
  :root {
    --backdrop: #efefee;
    --paper: #f5f5f4;
    --paper-shade: #ecebe9;
    --gold: #a8866a;
    --ink: #2e2b29;
    --grey: #8a8683;
    --spine: #dddcda;
  }
  * { margin: 0; padding: 0; box-sizing: border-box; }
  html, body { width: 1200px; height: 939px; overflow: hidden; background: var(--backdrop); }
  .canvas { position: relative; width: 1200px; height: 939px; }
  .sheet { position: absolute; background: var(--paper); overflow: hidden; }
  .pattern { position: absolute; background: linear-gradient(180deg, var(--paper-shade), #f0efed); }
  .rule { position: absolute; background: var(--gold); }

  .brand { position: absolute; text-align: center; color: var(--gold); }
  .brand__mark { display: block; margin: 0 auto; border-radius: 50%; background: var(--gold); }
  .brand__name { font-family: "Playfair Display", serif; font-weight: 600; line-height: 1.1; white-space: nowrap; }
  .brand__tag { font-family: "Montserrat", sans-serif; font-weight: 500; color: var(--ink); white-space: nowrap; }

  /* Letterhead */
  .letterhead { left: 208px; top: 88px; width: 358px; height: 507px; }
  .letter { position: absolute; left: 40px; right: 40px; font-family: "Tinos", serif; color: var(--ink); font-size: 6.2px; line-height: 1.45; text-align: justify; }
  .letter__recipient { top: 112px; }
  .letter__recipient strong { font-size: 7px; }
  .letter__body { top: 164px; }
  .letter__body p { margin-bottom: 6px; }
  .letter__closing { top: 338px; }
  .letter__signature { position: absolute; left: 40px; top: 350px; font-family: "Great Vibes", cursive; font-size: 19px; color: var(--ink); white-space: nowrap; }
  .footer { position: absolute; top: 442px; font-family: "Montserrat", sans-serif; font-size: 4.3px; line-height: 1.4; color: var(--grey); white-space: nowrap; }
  .footer--left { left: 40px; }
  .footer--right { right: 40px; text-align: right; }
  .footer--center { left: 0; right: 0; text-align: center; color: var(--gold); }
  .footer__web { position: absolute; left: 0; right: 0; top: 462px; text-align: center; font-family: "Montserrat", sans-serif; font-weight: 500; font-size: 6.5px; color: var(--gold); white-space: nowrap; }

  /* Folder */
  .folder { left: 628px; top: 66px; width: 422px; height: 532px; }
  .folder__spine { position: absolute; left: 8px; top: 0; bottom: 0; width: 1px; background: var(--spine); }

  /* Business cards */
  .card { width: 160px; height: 92px; left: 80px; }
  .card--back { top: 640px; }
  .card--front { top: 757px; }
  .card__text { position: absolute; left: 34px; font-family: "Montserrat", sans-serif; font-size: 3.8px; line-height: 1.5; color: var(--grey); white-space: nowrap; }
  .card__name { top: 12px; color: var(--ink); font-weight: 500; font-size: 4.4px; }
  .card__role { top: 19px; color: var(--gold); }
  .card__addr { top: 34px; }
  .card__web { top: 78px; color: var(--gold); }

  /* Envelopes */
  .envelope { top: 653px; height: 192px; }
  .envelope--window { left: 282px; width: 402px; }
  .envelope--flap { left: 722px; width: 430px; }
  .env__addr { position: absolute; left: 22px; top: 122px; font-family: "Montserrat", sans-serif; font-size: 4.4px; line-height: 1.5; color: var(--grey); white-space: nowrap; }
  .env__addr .web { color: var(--gold); margin-top: 4px; display: block; }
  .flap { position: absolute; left: 0; top: 0; width: 430px; height: 70px; }
</style>
</head>
<body>
<main class="canvas">

  <section class="sheet letterhead" aria-label="Papel timbrado">
    <div class="pattern" style="left:0;top:0;width:358px;height:26px" role="img" aria-label="Padrão decorativo de círculos entrelaçados em tom claro"></div>
    <div class="rule" style="left:0;top:26px;width:358px;height:2px"></div>
    <div class="brand" style="left:0;width:358px;top:38px">
      <span class="brand__mark" style="width:8px;height:8px"></span>
      <div class="brand__name" style="font-size:14px;margin-top:5px">Rubem Távora</div>
      <div class="brand__tag" style="font-size:5px;letter-spacing:1.6px;margin-top:2px">CIRURGIA PLÁSTICA</div>
    </div>
    <div class="letter letter__recipient"><strong>Mr. Jonh Doe</strong><br>Managing Director<br>Australia</div>
    <div class="letter letter__body">
      <p>Lorem ipsum dolor sit amet, consectetur adipisicing elit, sed do eiusmod tempor incididunt ut labore et dolore magna aliqua. Ut enim ad minim veniam, quis nostrud exercitation ullamco laboris nisi ut aliquip ex ea commodo consequat. Duis aute irure dolor in reprehenderit in voluptate velit esse cillum dolore eu fugiat nulla pariatur. Excepteur sint occaecat cupidatat non proident, sunt in culpa qui officia deserunt mollit anim id est laborum.</p>
      <p>Lorem ipsum dolor sit amet, consectetur adipisicing elit, sed do eiusmod tempor incididunt ut labore et dolore magna aliqua. Ut enim ad minim veniam, quis nostrud exercitation ullamco laboris nisi ut aliquip ex ea commodo consequat. Duis aute irure dolor in reprehenderit in voluptate velit esse cillum dolore eu fugiat nulla pariatur. Excepteur sint occaecat cupidatat non proident, sunt in culpa qui officia deserunt mollit anim id est laborum. Lorem ipsum dolor sit amet, consectetur adipisicing elit, sed do eiusmod tempor incididunt ut labore et dolore magna aliqua. Ut enim ad minim veniam, quis nostrud exercitation ullamco laboris nisi ut aliquip ex ea commodo consequat. Duis aute irure dolor in reprehenderit in voluptate velit esse cillum dolore eu fugiat nulla pariatur. Excepteur sint occaecat cupidatat non proident, sunt in culpa qui officia deserunt mollit anim id est laborum.</p>
      <p>Thank you for being one of our valued customers.</p>
    </div>
    <div class="letter letter__closing">Sincerely,</div>
    <div class="letter__signature">Jonh Doe</div>
    <div class="footer footer--left">Porto Celeste<br>Rua Clemente Vilaça, 418, 7° andar<br>Edificio Torre Quaresma<br>Porto Celeste - PC<br>(000) 9012-3456</div>
    <div class="footer footer--center">CRM/SC 52.807<br>CRM/SP 308.614</div>
    <div class="footer footer--right">Vila Aurora<br>Rua Lucas Bentim, 3180<br>Lucas Bentim Office, Cj 204<br>Vila Aurora - VA<br>(00) 90123-4567</div>
    <div class="footer__web">www.rubemtavorasilva.example</div>
    <div class="rule" style="left:0;top:477px;width:358px;height:2px"></div>
    <div class="pattern" style="left:0;top:479px;width:358px;height:28px" role="img" aria-label="Padrão decorativo de círculos entrelaçados em tom claro"></div>
  </section>

  <section class="sheet folder" aria-label="Pasta">
    <div class="folder__spine"></div>
    <div class="brand" style="left:0;width:422px;top:168px">
      <span class="brand__mark" style="width:18px;height:18px"></span>
      <div class="brand__name" style="font-size:27px;margin-top:12px">Rubem Távora</div>
      <div class="brand__tag" style="font-size:9px;letter-spacing:3.4px;margin-top:6px">CIRURGIA PLÁSTICA</div>
    </div>
    <div class="rule" style="left:0;top:420px;width:422px;height:3px"></div>
    <div class="pattern" style="left:0;top:423px;width:422px;height:109px" role="img" aria-label="Padrão decorativo de círculos entrelaçados em tom claro"></div>
  </section>

  <section class="sheet card card--back" aria-label="Cartão de visita, verso">
    <div class="pattern" style="left:0;top:0;width:160px;height:92px" role="img" aria-label="Padrão decorativo claro com perfil feminino sutil"></div>
    <div class="card__text card__name">DR. RUBEM TÁVORA</div>
    <div class="card__text card__role">cirurgião plástico</div>
    <div class="card__text card__addr">PORTO CELESTE - PC<br>(000) 9012-3456<br><br>VILA AURORA - VA<br>(00) 90123-4567</div>
    <div class="card__text card__web">RUBEMTAVORASILVA.EXAMPLE</div>
  </section>

  <section class="sheet card card--front" aria-label="Cartão de visita, frente">
    <div class="pattern" style="left:0;top:0;width:160px;height:92px" role="img" aria-label="Padrão decorativo de círculos entrelaçados em tom claro"></div>
    <div class="rule" style="left:35px;top:0;width:1px;height:92px"></div>
    <div class="rule" style="left:125px;top:0;width:1px;height:92px"></div>
    <div class="sheet" style="left:36px;top:0;width:89px;height:92px"></div>
    <div class="brand" style="left:36px;width:89px;top:30px">
      <span class="brand__mark" style="width:6px;height:6px"></span>
      <div class="brand__name" style="font-size:9px;margin-top:4px">Rubem Távora</div>
      <div class="brand__tag" style="font-size:3.4px;letter-spacing:1px;margin-top:1px">CIRURGIA PLÁSTICA</div>
    </div>
  </section>

  <section class="sheet envelope envelope--window" aria-label="Envelope ofício">
    <div class="pattern" style="left:205px;top:0;width:197px;height:192px" role="img" aria-label="Padrão decorativo de círculos entrelaçados em tom claro"></div>
    <div class="rule" style="left:201px;top:0;width:4px;height:192px"></div>
    <div class="brand" style="left:20px;width:92px;top:20px">
      <span class="brand__mark" style="width:8px;height:8px"></span>
      <div class="brand__name" style="font-size:11px;margin-top:5px">Rubem Távora</div>
      <div class="brand__tag" style="font-size:4px;letter-spacing:1.3px;margin-top:2px">CIRURGIA PLÁSTICA</div>
    </div>
    <div class="env__addr">PORTO CELESTE - PC<br>(000) 9012-3456<br><br>VILA AURORA - VA<br>(00) 90123-4567<span class="web">RUBEMTAVORASILVA.EXAMPLE</span></div>
  </section>

  <section class="sheet envelope envelope--flap" aria-label="Envelope carta">
    <div class="pattern" style="left:0;top:60px;width:430px;height:132px" role="img" aria-label="Padrão decorativo de círculos entrelaçados em tom claro"></div>
    <svg class="flap" viewBox="0 0 430 70" aria-hidden="true">
      <path d="M0 0 H430 V50 Q424 60 412 61 Q215 66 18 61 Q6 60 0 50 Z" fill="var(--gold)"/>
    </svg>
    <div class="brand" style="left:0;width:430px;top:20px;color:#fff">
      <div class="brand__name" style="font-size:13px">Rubem Távora</div>
    </div>
  </section>

</main>
</body>
</html>
```